QTL Newsletter

QTL provides mortgage processing outsource services to Mortgage Lenders in Australia and New Zealand. The company employs approximately 300 staff based in offices in Sydney, Melbourne, Brisbane, Adelaide and Perth in Australia and Auckland, New Zealand.
The company acquired a similar and much larger business in 2012 which is being integrated into the one business.
The objectives of a newsletter are to:
- Support the development of the company culture
- Develp a sense of "one team"
- Provide a communication forum for management and staff
I am seeking design options for the newsletter. We will develop/include specific content which will likley evolve over time.
A copy of the company brand gudelines and logo is attached for reference. Our website is currently going through a redesign. Additional information can be provided on request.

Target Market(s)

The target market for the newsletter is staff. This is a diverse group in terms of locations, age, gender, occupations etc.

Industry/Entity Type

Communication

Requirements
Must have
• Information to be included in the newsletter should include:
- Business results (activity, volumes, performance to budget)
- Client news section (recent developments, client profiling etc)
- New initiatives (update on key projects and new business initiatives, initiatives roadmap)
- Office news (news section for each office including new employees, team profile of the month, report on social events)
- CEO report

```html
<!DOCTYPE html>
<html lang="en">
<head>
<meta charset="utf-8">
<title>The Buzz – QTL Staff Newsletter</title>
<link rel="stylesheet" href="https://fonts.googleapis.com/css2?family=Carlito:wght@400;700&family=Cinzel:wght@400&family=Pinyon+Script&family=Cormorant+Garamond:wght@500&display=swap">
<style>
  :root {
    --brand-blue: #1c67a1;
    --ink: #111;
    --body-ink: #222;
    --muted: #555;
    --band-grey: #4b5661;
    --frame-grey: #8a8d91;
    --panel-grey: #d3d5d8;
    --rule-grey: #d9dbde;
    --accent-green: #95a93a;
    --highlight-blue: #38a7dd;
    --item-blue: #2a6ca6;
    --white: #fff;
  }
  * { margin: 0; padding: 0; box-sizing: border-box; }
  html, body { width: 848px; height: 1200px; overflow: hidden; background: var(--white); }
  .page { position: relative; width: 848px; height: 1200px; font-family: "Carlito", "Calibri", sans-serif; color: var(--body-ink); }

  .issue-date { position: absolute; left: 36px; top: 24px; font-family: "Cormorant Garamond", serif; font-size: 18px; letter-spacing: 3.4px; color: var(--muted); }

  .masthead { position: absolute; left: 0; top: 52px; width: 848px; height: 170px; background: var(--brand-blue); }
  .masthead-the { position: absolute; left: 130px; top: 8px; font-family: "Pinyon Script", cursive; font-size: 190px; line-height: 1; color: var(--white); }
  .masthead-buzz { position: absolute; left: 392px; top: 66px; font-family: "Cinzel", serif; font-size: 142px; line-height: 1; color: var(--white); letter-spacing: 2px; }
  .brand-box { position: absolute; left: 692px; top: 52px; width: 98px; height: 50px; background: var(--white); display: flex; align-items: center; justify-content: center; }
  .brand-name { font-family: "Carlito", sans-serif; font-weight: 700; font-size: 30px; color: var(--brand-blue); letter-spacing: 1px; }

  .tagline-band { position: absolute; left: 0; top: 230px; width: 848px; height: 20px; background: var(--band-grey); color: var(--white); font-family: "Cormorant Garamond", serif; font-size: 15.5px; letter-spacing: 3.3px; line-height: 20px; padding-left: 34px; white-space: nowrap; }

  .frame-left { position: absolute; left: 58px; top: 250px; width: 1px; height: 910px; background: var(--frame-grey); }
  .frame-bottom { position: absolute; left: 58px; top: 1160px; width: 733px; height: 1px; background: var(--frame-grey); }
  .frame-right { position: absolute; left: 790px; top: 250px; width: 1px; height: 42px; background: var(--frame-grey); }
  .column-divider { position: absolute; left: 577px; top: 292px; width: 1px; height: 840px; background: var(--frame-grey); }

  .section-title { position: absolute; left: 89px; top: 294px; font-weight: 700; font-size: 58px; line-height: 1; color: var(--ink); letter-spacing: -0.5px; }
  .section-lead { position: absolute; left: 90px; top: 362px; font-size: 15.5px; color: var(--ink); }

  .photo { position: absolute; }
  .photo-team { left: 30px; top: 405px; width: 298px; height: 193px; background: linear-gradient(135deg, #c9d3dd 0%, #9fb3c6 45%, #d9c2b0 100%); }
  .photo-employee { left: 348px; top: 983px; width: 185px; height: 149px; background: linear-gradient(160deg, #eef1f4 0%, #d8dde2 55%, #b89a80 100%); }

  .lead-story { position: absolute; left: 90px; top: 399px; width: 443px; font-size: 13.4px; line-height: 18.55px; color: var(--body-ink); }
  .lead-story .photo-space { float: left; width: 253px; height: 205px; }
  .lead-story p { text-indent: 16px; }
  .lead-story p.first { text-indent: 0; }
  .drop-cap { float: left; font-size: 54px; line-height: 44px; margin: 2px 3px 0 0; color: var(--accent-green); font-weight: 700; }

  .section-rule { position: absolute; left: 92px; top: 943px; width: 438px; height: 12px; background: var(--rule-grey); }

  .highlight-title { position: absolute; left: 90px; top: 976px; font-weight: 700; font-size: 22px; color: var(--highlight-blue); letter-spacing: 0.3px; }
  .highlight-body { position: absolute; left: 90px; top: 1003px; width: 252px; font-size: 13.4px; line-height: 18.5px; }

  .office-panel { position: absolute; left: 600px; top: 292px; width: 248px; height: 840px; background: var(--panel-grey); }
  .office-title { position: absolute; left: 38px; top: 18px; font-weight: 700; font-size: 44px; color: var(--ink); letter-spacing: 0.5px; }
  .office-script { position: absolute; left: 58px; top: 48px; font-family: "Pinyon Script", cursive; font-size: 58px; color: var(--brand-blue); line-height: 1; }
  .news-item { position: absolute; left: 38px; width: 185px; font-size: 13.4px; line-height: 18.5px; color: var(--body-ink); }
  .news-item h3 { font-size: 13.4px; font-weight: 700; color: var(--item-blue); letter-spacing: 0.4px; }
  .news-item-1 { top: 164px; }
  .news-item-2 { top: 460px; }
</style>
</head>
<body>
<div class="page">
  <div class="issue-date">FEBRUARY 12, 2013</div>

  <header class="masthead">
    <div class="masthead-the">The</div>
    <div class="masthead-buzz">BUZZ</div>
  </header>
  <div class="brand-box"><span class="brand-name">QTL</span></div>
  <div class="tagline-band">FORUM FOR MANAGEMENT &amp; STAFF OF QUAY TRANSACTION LENDING</div>

  <div class="frame-left"></div>
  <div class="frame-bottom"></div>
  <div class="frame-right"></div>
  <div class="column-divider"></div>

  <h1 class="section-title">Team News</h1>
  <div class="section-lead">Lead item to draw people into the newsletter</div>

  <div class="photo photo-team" role="img" aria-label="Photo of a smiling group of colleagues"></div>

  <article class="lead-story">
    <div class="photo-space"></div>
    <p class="first"><span class="drop-cap">Q</span>uament et am rest, sent eos simaximet optur?Pudiorr untiusandi acerit omnia ducienietus.</p>
    <p>Agnihit iuresto rempost, nonse cor autat voluptio ipsus ipsamusdae nonetur, soluptatus. Odiat. Dia sit, officiatur, inihil id etur res estio dolorerrorem et, con cus, ipiet aute vel et es alit init quas aut venisitatum raes inum excepedia et exped quiaectem quae qui dolore omnis aceritium rempos nat eation res es explandes molor samendit haribusam et evelend isquame ndempos volut is et accus molut pos aliqui ad maionet uritates dolupta sperferum eicae lautem. Ut fugit, optaspellab ipsus eicto quam, consequ atectamet, consequam, te illictem ant voluptis magnat eatestio vent.</p>
    <p>Exero volenem hitaquas errorio. Ga. Ut aute cupti cusda am, sitem sumque quid quia consequo ma inia essi ut enis et pratur accae quaerias aliqui con explique susam estianihite aut et verovit venduntur, inulloreiur sumet, ius aut andandi nes est verepudit quibus rehenti usant.</p>
    <p>Excea excea sitiunt. Osa eum doluptio consed ex ea dit aut ex eumquam rem rerfercid quiassim sitaes illorec aecerum consed quae nienimo lorep­rum dempor aut voluptas dolor autem. Et illorae volorio molore cuptatiatur Odia sumqui beaquam dolesti quiam autem name eos estem ex evendunt min ea quate vit min nonem. Nequasperias quidenti que voluptatis aliquo es rerro est re expliquiande rehent expeles audi test, occaborpor maxim recest, offici ius at volupta quam ducitius.</p>
  </article>

  <div class="section-rule"></div>

  <h2 class="highlight-title">EMPLOYEE HIGHLIGHT</h2>
  <div class="highlight-body">Agnihit iuresto rempost, nonse cor autat voluptio ipsus ipsamusdae nonetur, soluptatus.Odiat. Dia sit, officiatur, inihil id etur res estio dolorerrorem et, con cus, ipiet aute dolore omnis aceritium rempos nat eation re es explandes molor samendit haribusam et evelend isquame ndempos volut is et</div>
  <div class="photo photo-employee" role="img" aria-label="Portrait photo of the featured employee"></div>

  <aside class="office-panel">
    <div class="office-title">OFFICE</div>
    <div class="office-script">News</div>
    <section class="news-item news-item-1">
      <h3>NEWS ITEM 1</h3>
      <p>Agnihit iuresto rempost, nonse cor autat voluptio ipsus ipsamusdae nonetur, soluptatus. Odiat. Dia sit, officiatur, inihil id etur res estio dolorerrorem et, con cus, ipiet aute vel et es alit init quas aut venisitatum raes inum excepedia et exped quiaectem quae qui dolore omnis aceritium rempos nat eation res es explandes molor samendit haribusam et evelend isquame ndempos volut is et</p>
    </section>
    <section class="news-item news-item-2">
      <h3>NEWS ITEM 2</h3>
      <p>ccus molut pos aliqui ad maionet uritates dolupta sperferum eicae lautem. Ut fugit, optaspellab ipsus eicto quam, consequ atectamet, consequam, te illictem ant voluptis magnat eatestio vent. Exero volenem hitaquas errorio. Ga. Ut aute cupti cusda am, sitem sumque quid quia consequo ma inia essi ut enis et pratur accae quaerias aliqui con explique susam estianihite aut et verovit venduntur, inulloreiur sumet, ius aut andandi nes est verepudit quibus rehenti usant. Excea excea sitiunt. Osa eum doluptio consed ex ea dit aut ex eumquam.</p>
    </section>
  </aside>
</div>
</body>
</html>
```